Envelope design

We need a envelope design for a professional services firm called Brindlemoor Tax Advisory Inc. The firm is essentially a very specialized tax accounting firm - instead of serving the end consumer, we support other public accounting firms in the area of Canadian and U.S. tax advisory and compliance (i.e. they call us on tax issues too complex for the general practitioner). Our byline is "Tax Support Services for Public Accounting Firms". Our postcard should utilize our logo and be based on colours present in our logo (see file attached). The final design needs to convey professionalism and trustworthiness (we're hired by accountants after all!) while being creative and eye-catching. Eye-catching is critical, since many prospective recipients will not have heard from me before and I want them to read the postcard.
At lot of design work has already been done here. I've attached a number of sample files showing logo and letterhead designs. Please note that the letterhead hasn't yet been updated for the new logo. This is happening in a separate design competition.
Updates
Project Deadline Extended Reason: Deadline is extended because I am pricing the extra cost of having colour right to the edge of the envelopes. This will help me design on final design. Pricing should come in on Monday. Added Saturday, February 20, 2016

```html
<!DOCTYPE html>
<html lang="en">
<head>
<meta charset="utf-8">
<title>Brindlemoor Tax Advisory Inc. – Envelope</title>
<link rel="stylesheet" href="https://fonts.googleapis.com/css2?family=Cinzel:wght@500&family=Lato:wght@400&display=swap">
<style>
  :root {
    --backdrop: #e9e7e4;
    --paper: #ffffff;
    --band: #141414;
    --ink: #1e1e1e;
    --white: #ffffff;
    --gold: #f6ae2d;
    --shadow: rgba(0, 0, 0, 0.28);
  }
  * { margin: 0; padding: 0; box-sizing: border-box; }
  html, body {
    width: 1200px; height: 1000px; overflow: hidden;
    background: var(--backdrop);
  }
  .canvas { position: relative; width: 1200px; height: 1000px; }

  .envelope {
    position: absolute; left: 195px; width: 810px; height: 351px;
    background: var(--paper);
    box-shadow: 4px 6px 10px var(--shadow);
    overflow: hidden;
  }
  .envelope--front { top: 148px; }
  .envelope--back { top: 556px; }

  .header-band {
    position: absolute; left: 0; top: 0; width: 100%; height: 110px;
    background: var(--band);
  }
  .brand {
    position: absolute; left: 93px; top: 22px;
    display: flex; align-items: flex-start; gap: 13px;
  }
  .brand__square {
    width: 56px; height: 56px; background: var(--gold); flex: none;
  }
  .brand__text { color: var(--white); }
  .brand__name {
    font-family: "Cinzel", serif; font-weight: 500;
    font-size: 35px; line-height: 36px; letter-spacing: 0.5px;
    white-space: nowrap;
    border-bottom: 1.5px solid var(--white);
    padding-bottom: 1px;
  }
  .brand__byline {
    font-family: "Cinzel", serif; font-weight: 500;
    font-size: 15px; line-height: 18px; letter-spacing: 3.6px;
    margin-top: 3px; white-space: nowrap;
  }

  .return-address {
    position: absolute; left: 0; right: 0; top: 302px;
    text-align: center;
    font-family: "Lato", sans-serif; font-size: 9.5px; line-height: 16px;
    color: var(--ink);
  }

  .flap {
    position: absolute; left: 0; top: 0; width: 100%; height: 127px;
    background: var(--band);
    border-radius: 0 0 26px 26px;
  }
  .flap__square {
    position: absolute; left: 361px; top: 19px;
    width: 88px; height: 88px; background: var(--gold);
  }
</style>
</head>
<body>
<main class="canvas">
  <section class="envelope envelope--front" aria-label="Envelope front">
    <header class="header-band">
      <div class="brand">
        <span class="brand__square" aria-hidden="true"></span>
        <div class="brand__text">
          <div class="brand__name">BRINDLEMOOR TAX ADVISORY</div>
          <div class="brand__byline">TAX SUPPORT FOR PUBLIC ACCOUNTING FIRMS</div>
        </div>
      </div>
    </header>
    <address class="return-address" style="font-style: normal;">
      18-410 Larchfield Avenue, Dartmouth, Nova Scotia, Canada B3B 2K4<br>
      T: 902.555.0148 &nbsp;|&nbsp; F: 902.555.0172 &nbsp;|&nbsp; E: owen@brindlemoortax.services<br>
      www.brindlemoortax.services
    </address>
  </section>

  <section class="envelope envelope--back" aria-label="Envelope back">
    <div class="flap">
      <span class="flap__square" aria-hidden="true"></span>
    </div>
  </section>
</main>
</body>
</html>
```